Come crowdsource a Web Design for a brazilian crowdsource Startup!

> NAME OF OUR STARTUP:
Vantremo

> DESCRIPTION OF OUR STARTUP:
We are a crowdsourcing startup in Brazil providing consultancy and technology to support other companies to crowdsource their projects.
We also operate doing big crowdsource campaings related to polemic subjects in Brazil.

> WHAT ARE OUR TARGET AUDIENCE?
Our target audience are young people around 20-35 years old.
Generation Y (Millennial Generation)

> WHAT IS OUR INDUSTRY?
Internet, web

> WHAT DO WE NEED?
We need a Web Design for our first site.

We need 5 pages:
- Home
- What is Crowdsourcing?
- Solutions
- About Us
- Blog
- A box for the "Contact" tab (this is not a page)

Please, find attached a Layout Sketch of what I've imagined.

Lets talk about the sketch:
Well, first of all, it's a SKETCH, so you don't have to send proposals exactly as the sketch. The sketch is just to show how I've imagined the ditribution of the content boxes. For example, the menu bar doesnt need to be a rectangle exactly like the sketch, but, I would like to have the menu on the right side of the logo. Also, you will see that the boxes are all squeezed, of course I dont want them soo squeezed! Again, its juust a SKETCH!

About the images on the sketch:
IMG1 - Some nice and simple image related to collectivity or related to crowdsourcing or maybe use our O logo.

IMG2 - Some simple and creative image related to Consultancy. It doesnt need to be so obvious.

IMG3 - Some simple and creative image related to Web 2.0 Software Technology. It doesnt need to be so obvious.

IMG4 - Some simple and creative image related to a full package of Consultancy + Technology. It doesnt need to be so obvious.

IMG5 - Some nice and simple image related to collectivity or related to crowdsourcing.

IMG6 - Some nice and simple image related to Ideation. Maybe a light bulb? I dont know, be creative!

IMG7 - Some nice and simple image related to Crowdlabor. I dont know, be creative!

IMG8 - Some nice and simple image related to CrowdFeedback. Maybe a megaphone? A loudspeaker? I dont know, be creative!

IMG9 - Some nice and simple image related to us! Maybe our O logo ? I dont know, be creative!

THE CONTACT SIDE BAR - we need a nice and simple contact side bar. By the way, on the sketch this bar is shown only at the homepage, but when the site becomes real this bar will stay along all the pages.

THE CONTACT BOX - we need a nice and simple contact box.

ABOUT THE COLORS TO USE: we would like some color to our background and titles. We like colors similars to our logo: really light blue ? light green/blue ? light grey ? light orange ? I dont know, you guys knows more about that then me =)

PLIMBOOK SHARE/LIKE BUTTON: We would like a plimbook share/like button somewhere on the site!

ABOUT THE ATTACHED FILES:

ADDITIONALS:
> The name Vantremo comes from "collectivity". With our name we want to pass the idea of the collectivity from the crowdsource work model.

> Our communication is directed to the Generation Y.

> Remember, we are a Startup! So we need a modern and simple site, something like the web 2.0 trends. It must be beautiful =)

> We arent a serious company. We are a young and fun company! Please, dont come with old fashionable company sites.

> Be creative =] !

Target Market(s)

Our target audience are young people around 20-35 years old. Generation Y (Millennial Generation)

Industry/Entity Type

Communication

Requirements
Must have
• We need a Web Design for our first site.

We need 5 pages:
- Home
- What is Crowdsourcing?
- Solutions
- About Us
- Blog

ABOUT THE COLORS TO USE: we would like some color to our background and titles. We like colors similars to our logo: really light blue ? light green/blue ? light grey ? light oranges ? I dont know, you guys knows more about that then me =)

Should not have
• Poor/serious/old fashionable designs

```html
<!DOCTYPE html>
<html lang="en">
<head>
<meta charset="utf-8">
<title>Vantremo — Home</title>
<link rel="stylesheet" href="https://fonts.googleapis.com/css2?family=Abel&family=Archivo+Narrow:wght@700&family=Open+Sans:wght@400;600;700&family=Raleway:wght@800&display=swap">
<style>
  :root {
    --teal: #22a7b3;
    --teal-bright: #3bb4c1;
    --teal-deep: #0e4e57;
    --teal-text: #1f9dab;
    --nav-line: #3a3a3c;
    --card-grey: #dcdcdc;
    --frame-grey: #e6e6e6;
    --body-text: #4a4a4a;
    --orange: #fbb131;
    --social-dark: #202022;
    --social-blue: #2f4f96;
    --white: #ffffff;
  }
  * { box-sizing: border-box; margin: 0; padding: 0; }
  html, body { width: 1073px; height: 1200px; overflow: hidden; background: var(--white); }
  .page {
    position: relative; width: 1004px; height: 1123px;
    transform: scale(1.0687); transform-origin: 0 0;
    font-family: "Open Sans", sans-serif; color: var(--body-text);
  }

  /* Top navigation */
  .main-nav {
    position: absolute; left: 0; top: 0; width: 1004px; height: 52px;
    background: linear-gradient(#242426, #141415);
  }
  .main-nav ul { list-style: none; display: flex; position: absolute; left: 22px; top: 0; }
  .main-nav li {
    height: 52px; padding: 0 26px; line-height: 52px;
    font-family: "Abel", sans-serif; font-size: 24px; color: var(--white);
    border-right: 1px solid var(--nav-line);
  }
  .main-nav li.is-active { background: var(--teal-bright); color: #0f3338; border-right-color: #0d0d0d; }
  .main-nav .search-button {
    position: absolute; left: 953px; top: 0; width: 28px; height: 52px;
    background: var(--teal-bright); display: flex; align-items: center; justify-content: center;
  }

  /* Hero */
  .hero { position: absolute; left: 0; top: 52px; width: 1004px; height: 510px; background: var(--teal); }
  .brand {
    position: absolute; left: 32px; top: 38px; display: flex; align-items: center; gap: 10px;
    font-family: "Open Sans", sans-serif; font-weight: 700; font-size: 40px; line-height: 52px; color: var(--white);
  }
  .brand .brand-dot { width: 28px; height: 28px; border-radius: 50%; background: var(--white); }
  .social-links { position: absolute; left: 725px; top: 23px; display: flex; gap: 5px; }
  .social-links a {
    width: 47px; height: 47px; background: var(--social-dark); color: var(--white);
    font-size: 8px; font-weight: 600; text-decoration: none;
    display: flex; align-items: center; justify-content: center;
  }
  .social-links a.plimbook { background: var(--social-blue); }
  .mission { position: absolute; left: 30px; top: 182px; width: 370px; }
  .mission h1 {
    font-family: "Archivo Narrow", sans-serif; font-weight: 700; font-size: 34px; color: var(--teal-deep);
  }
  .mission p { margin-top: 12px; font-size: 14px; line-height: 24px; color: var(--white); text-align: justify; }
  .mission p strong { color: #0b1c1e; font-weight: 600; }
  .button-more {
    position: absolute; left: 307px; top: 371px; width: 90px; height: 31px;
    background: var(--white); border: 1px solid #b9dfe3; color: var(--teal-text);
    font-size: 12px; font-weight: 700; line-height: 29px; text-align: center;
  }
  .slider-back {
    position: absolute; left: 446px; top: 120px; width: 500px; height: 350px;
    background: #f1f1f1; transform: rotate(-4deg); box-shadow: 0 3px 8px rgba(0,0,0,.25);
  }
  .slider-back .accent { position: absolute; left: 10px; top: 14px; width: 60px; height: 310px; background: var(--orange); }
  .slider {
    position: absolute; left: 493px; top: 100px; width: 488px; height: 354px;
    background: var(--frame-grey); border-radius: 6px; box-shadow: 0 3px 8px rgba(0,0,0,.3);
  }
  .slider .slide {
    position: absolute; left: 10px; top: 10px; width: 468px; height: 304px; border-radius: 6px;
    background:
      radial-gradient(circle at 38% 48%, #c9d3ec 0, #a9b7df 22%, rgba(140,157,206,0) 45%),
      linear-gradient(100deg, #9eaedb 0%, #8798cb 60%, #4a5a86 82%, #2a3550 100%);
  }
  .slider-dots { position: absolute; left: 189px; top: 324px; display: flex; gap: 7px; }
  .slider-dots span { width: 16px; height: 16px; border-radius: 50%; background: #1e1e20; }
  .slider-dots span.is-current { background: var(--teal-bright); }

  /* Welcome */
  .welcome { position: absolute; left: 22px; top: 580px; width: 959px; }
  .welcome h2 {
    font-family: "Raleway", sans-serif; font-weight: 800; font-size: 24px; line-height: 34px; color: var(--teal-text);
  }
  .welcome .rule { position: absolute; left: 283px; top: 24px; width: 676px; border-top: 3px dotted #c9c9c9; }
  .welcome p { margin-top: 8px; font-size: 12.5px; line-height: 24px; text-align: justify; }
  .welcome .read-more { position: absolute; right: 2px; top: 151px; font-size: 13px; color: var(--teal-text); }

  /* Service cards */
  .service {
    position: absolute; top: 780px; width: 300px; height: 235px;
    border: 1px solid #e0e0e0; background: var(--white); box-shadow: 0 8px 8px -6px rgba(0,0,0,.2);
  }
  .service h3 {
    position: absolute; left: 4px; top: 5px; width: 290px; height: 52px;
    font-size: 18px; font-weight: 600; line-height: 52px; text-align: center;
    background: var(--card-grey); color: var(--teal-text);
  }
  .service h3::before {
    content: ""; position: absolute; left: 139px; top: 0;
    border: 6px solid transparent; border-top-color: var(--white);
  }
  .service.is-featured h3 { background: var(--teal-bright); color: #121212; }
  .service .service-image { position: absolute; left: 4px; top: 57px; width: 290px; height: 173px; }
  .consultancy { left: 21px; }
  .technology { left: 351px; }
  .combined { left: 681px; }
  .consultancy .service-image { background: radial-gradient(ellipse at 55% 40%, #4a4644 0, #2c2c2f 55%, #1b1c1f 100%); }
  .technology .service-image { background: radial-gradient(ellipse at 50% 45%, #e4e8ee 0, #c7ccd3 45%, #8d9197 80%, #55585c 100%); }
  .combined .service-image { background: radial-gradient(ellipse at 72% 40%, #e8d6c6 0, #dfe3e8 40%, #f3f5f7 75%); }

  /* Footer */
  .site-footer { position: absolute; left: 0; top: 1071px; width: 1004px; height: 52px; background: var(--teal); }
  .footer-nav { position: absolute; left: 20px; top: 16px; display: flex; font-size: 13px; color: var(--white); }
  .footer-nav span + span::before { content: "|"; color: #7fd0d8; margin: 0 10px; }
  .footer-nav .is-active { color: #0f3338; }
  .footer-brand {
    position: absolute; left: 498px; top: -28px; width: 172px; height: 56px;
    background: var(--teal); border-radius: 28px 28px 0 0;
    font-weight: 700; font-size: 28px; line-height: 54px; text-align: center; color: var(--white);
  }
  .copyright { position: absolute; right: 24px; top: 17px; font-size: 12px; color: var(--white); }
</style>
</head>
<body>
<div class="page">
  <nav class="main-nav">
    <ul>
      <li class="is-active">Home</li>
      <li>About Us</li>
      <li>What is Crowdsourcing?</li>
      <li>Solutions</li>
      <li>Blog</li>
    </ul>
    <div class="search-button">
      <svg width="16" height="16" viewBox="0 0 16 16"><circle cx="6.5" cy="6.5" r="4.5" fill="none" stroke="#fff" stroke-width="2.2"/><line x1="10" y1="10" x2="14.5" y2="14.5" stroke="#fff" stroke-width="2.6" stroke-linecap="round"/></svg>
    </div>
  </nav>

  <header class="hero">
    <div class="brand"><span class="brand-dot"></span>Vantremo</div>
    <div class="social-links">
      <a class="plimbook">plimbook</a>
      <a>Chirra</a>
      <a>
        <svg width="20" height="20" viewBox="0 0 20 20"><circle cx="4" cy="16" r="2.5" fill="#fff"/><path d="M2 9a9 9 0 0 1 9 9" fill="none" stroke="#fff" stroke-width="2.6"/><path d="M2 3a15 15 0 0 1 15 15" fill="none" stroke="#fff" stroke-width="2.6"/></svg>
      </a>
      <a>Orbly</a>
      <a>Pinvo</a>
    </div>

    <section class="mission">
      <h1>Vantremo Mission:</h1>
      <p><strong>Here we tell our mission in a few lines.</strong> Lorem ipsum dolor sit amet, consectetur adipiscing elit. Vestibulum lectus ante, lacinia eu ultrices non, pellentesque at elit.</p>
    </section>
    <div class="button-more">More Info »</div>

    <div class="slider-back"><div class="accent"></div></div>
    <div class="slider">
      <div class="slide" role="img" aria-label="A hand holding a magnifying glass over a crowd of people icons"></div>
      <div class="slider-dots"><span class="is-current"></span><span></span><span></span><span></span><span></span></div>
    </div>
  </header>

  <section class="welcome">
    <h2>Welcome to vantremo</h2>
    <div class="rule"></div>
    <p>Lorem ipsum dolor sit amet, consectetur adipiscing elit. Nam ultricies lacinia eros, vitae ultricies justo convallis a. Vestibulum ante ipsum primis in faucibus orci luctus et ultrices posuere cubilia Curae; Fusce porta, leo eu condimentum commodo, nunc purus facilisis lectus, quis consequat sem nisl eget elit. In rhoncus mollis sem, convallis fermentum arcu fermentum at. Phasellus consequat condimentum felis, eget rutrum libero hendrerit eget. Sed ullamcorper dictum nulla eu rhoncus. Curabitur tellus massa, congue sodales accumsan eu, sodales sed turpis. Aenean ultrices aliquet ligula sed facilisis.</p>
    <span class="read-more">Read more...</span>
  </section>

  <article class="service consultancy is-featured">
    <h3>Consultancy</h3>
    <div class="service-image" role="img" aria-label="Business team meeting around documents, dimmed, with search and link icons">
      <svg width="290" height="173" viewBox="0 0 290 173">
        <circle cx="124" cy="84" r="20" fill="#3bb4c1" stroke="#fff" stroke-width="2"/>
        <circle cx="121" cy="81" r="7" fill="none" stroke="#fff" stroke-width="2.5"/>
        <line x1="126" y1="86" x2="132" y2="92" stroke="#fff" stroke-width="3" stroke-linecap="round"/>
        <circle cx="173" cy="84" r="20" fill="#3bb4c1" stroke="#fff" stroke-width="2"/>
        <rect x="163" y="80" width="12" height="7" rx="3.5" fill="none" stroke="#fff" stroke-width="2.5" transform="rotate(-45 169 83)"/>
        <rect x="171" y="80" width="12" height="7" rx="3.5" fill="none" stroke="#fff" stroke-width="2.5" transform="rotate(-45 177 83)"/>
      </svg>
    </div>
  </article>

  <article class="service technology">
    <h3>Techonlogy</h3>
    <div class="service-image" role="img" aria-label="Technician with a laptop in front of server equipment"></div>
  </article>

  <article class="service combined">
    <h3>Consultancy + Technology</h3>
    <div class="service-image" role="img" aria-label="Support team with headsets at a laptop"></div>
  </article>

  <footer class="site-footer">
    <div class="footer-brand">Vantremo</div>
    <div class="footer-nav">
      <span class="is-active">Home</span><span>About Us</span><span>What is Crowdsourcing?</span><span>Solutions</span><span>Blog</span>
    </div>
    <div class="copyright">Copyright © 2013 Vantremo.&nbsp; All Rights Reserved.</div>
  </footer>
</div>
</body>
</html>
```